Coffee and Plastics

I am looking for a completely new site that shows the products we have. Our current site is www.morvelbrewsupply.com. We are open minded to what designers come up with. Our current site is www.morvelbrewsupply.com. You can you the information from there to start the site. I need these tabs on the main home page. ( Home, Coffee & Tea, Condiments, and Paper and Plastics, and Contact.) You can take photos and info from my Current site. In products page.
I will be uploading info and photo for paper and plastics.
Look and feel
Each slider illustrates characteristics of the customer's brand and the style your logo design should communicate.

```html
<!DOCTYPE html>
<html lang="en">
<head>
<meta charset="utf-8">
<title>Morvel Brew Supply</title>
<link href="https://fonts.googleapis.com/css2?family=Open+Sans:wght@400;600;700&display=swap" rel="stylesheet">
<style>
  :root {
    --ink: #333333;
    --bar: #333333;
    --white: #ffffff;
    --gold: #e3c06a;
    --text: #3a3a3a;
    --roast-dark: #2b2623;
    --roast-mid: #5a4537;
    --roast-light: #8a6a52;
    --seal: #a9d5db;
  }
  * { box-sizing: border-box; margin: 0; padding: 0; }
  html, body { width: 1074px; height: 1200px; overflow: hidden; background: var(--white); }
  body { position: relative; font-family: "Open Sans", Arial, sans-serif; color: var(--text); }

  .topbar { position: absolute; left: 0; top: 0; width: 1074px; height: 43px; background: var(--bar); }
  .monogram { position: absolute; left: 62px; top: 10px; color: var(--white); font-weight: 700; font-size: 18px; letter-spacing: 1px; }
  .main-nav { position: absolute; right: 62px; top: 0; display: flex; gap: 27px; height: 43px; align-items: center; }
  .main-nav a { color: var(--white); text-decoration: none; font-size: 13.5px; }

  .brand { position: absolute; left: 62px; top: 118px; display: flex; align-items: center; gap: 12px; }
  .brand-square { width: 22px; height: 22px; background: #111; }
  .brand-name { font-size: 30px; font-weight: 700; color: #111; letter-spacing: 1px; }

  .social { position: absolute; top: 98px; left: 828px; display: flex; gap: 9px; }
  .social span { width: 38px; height: 38px; border-radius: 50%; background: var(--gold); display: block; }
  .callout { position: absolute; right: 63px; top: 144px; text-align: right; color: var(--gold); font-size: 19.5px; line-height: 22px; letter-spacing: .5px; font-weight: 600; }

  .hero { position: absolute; left: 62px; top: 235px; width: 950px; height: 413px; overflow: hidden;
    background: radial-gradient(ellipse at 75% 35%, var(--roast-light), var(--roast-mid) 45%, var(--roast-dark) 100%); }
  .hero-shade { position: absolute; left: 0; top: 0; width: 458px; height: 413px; background: rgba(40,36,34,.55); }
  .hero-copy { position: absolute; left: 36px; top: 34px; width: 390px; color: var(--white); text-shadow: 0 1px 3px rgba(0,0,0,.7); }
  .hero-kicker { font-size: 17px; font-weight: 600; }
  .hero-title { font-size: 28px; font-weight: 600; margin-top: 6px; letter-spacing: .3px; }
  .hero-copy p { font-size: 14px; line-height: 17px; margin-top: 18px; font-weight: 600; }
  .hero-copy .hero-title + p { margin-top: 28px; }
  .range-link { position: absolute; right: 0; height: 41px; background: var(--bar); color: var(--white);
    font-size: 13.5px; font-weight: 600; display: flex; align-items: center; justify-content: flex-end; padding-right: 9px;
    clip-path: polygon(12px 0, 100% 0, 100% 100%, 12px 100%, 0 50%); }

  .info { position: absolute; top: 671px; }
  .info h2 { font-size: 17px; font-weight: 600; color: var(--ink); letter-spacing: .3px; }
  .info p { font-size: 13.5px; line-height: 17.2px; margin-top: 6px; }
  .info-products { left: 60px; width: 445px; }
  .info-quality { left: 552px; width: 450px; }

  .guarantee { position: absolute; left: 250px; top: 854px; font-size: 17.5px; color: var(--text); }
  .seal { position: absolute; left: 882px; top: 810px; width: 104px; height: 104px; border-radius: 50%; background: var(--seal); }

  .partners { position: absolute; left: 0; top: 954px; width: 1074px; height: 200px; background: var(--bar); }
  .partners h3 { text-align: center; color: var(--white); font-size: 17px; font-weight: 600; margin-top: 34px; letter-spacing: .4px; }
  .partner { position: absolute; border-radius: 4px; }

  .copyright { position: absolute; left: 62px; top: 1166px; font-size: 13.5px; color: var(--text); }
</style>
</head>
<body>
  <header class="topbar">
    <div class="monogram">MBS</div>
    <nav class="main-nav">
      <a href="#">HOME</a><a href="#">COFFEE &amp; TEA</a><a href="#">CONDIMENTS</a><a href="#">PAPER &amp; PLASTICS</a><a href="#">CONTACT</a>
    </nav>
  </header>

  <div class="brand"><span class="brand-square"></span><span class="brand-name">MORVEL BREW SUPPLY</span></div>

  <div class="social" aria-label="Social links"><span></span><span></span><span></span><span></span></div>
  <div class="callout">CALL US: 1-800-555-0142<br>MON-FRI 9-5 CENTRAL TIME</div>

  <section class="hero" role="img" aria-label="Roasted coffee beans spilling from a burlap sack onto a dark stone surface">
    <div class="hero-shade"></div>
    <div class="hero-copy">
      <div class="hero-kicker">WELCOME TO</div>
      <div class="hero-title">MORVEL BREW SUPPLY</div>
      <p>We are a family-owned and operated business based in Calder Springs.</p>
      <p>Since the opening of Morvel Brew Supply plant in 1995, we have become the region's premier independently owned coffee packaging company.</p>
      <p>Our success relies solely on the principle of selling only the freshest, highest-quality in-room coffee available.</p>
    </div>
    <a class="range-link" style="top:245px;width:296px">BROWSE OUR RANGE OF COFFEE &amp; TEA</a>
    <a class="range-link" style="top:295px;width:296px">BROWSE OUR RANGE OF CONDIMENTS</a>
    <a class="range-link" style="top:346px;width:363px">BROWSE OUR RANGE OF PAPER &amp; PLASTIC WARE</a>
  </section>

  <section class="info info-products">
    <h2>PRODUCTS WE SUPPLY</h2>
    <p>Morvel Brew Supply packages and supplies in-room coffee, tea products, and condiments. Whether we're supplying a 50-room Hotel or a 500-room grand resort, we have the distribution capacity to fill your rooms with the most aromatic and robust coffees and teas available at competitive prices.</p>
  </section>
  <section class="info info-quality">
    <h2>OUR QUALITY ASSURANCE</h2>
    <p>Morvel Brew Supply is continuously striving for ways to improve quality and product appearance to meet the highest standards in today's franchises and independent hotels. We are very aware that our success depends entirely upon maintaining our customers' confidence in our products, so we pay close attention to your needs every step of the way.</p>
  </section>

  <p class="guarantee">We guarantee all of our products will meet your level of satisfaction.</p>
  <div class="seal" role="img" aria-label="Satisfaction guaranteed seal"></div>

  <section class="partners">
    <h3>SERVING FINE ESTABLISHMENTS EVERYWHERE!</h3>
    <div class="partner" style="left:104px;top:92px;width:98px;height:60px;background:#3a2f6e"></div>
    <div class="partner" style="left:234px;top:92px;width:106px;height:60px;background:#2c4a7a"></div>
    <div class="partner" style="left:380px;top:90px;width:94px;height:62px;background:#2f7a4c"></div>
    <div class="partner" style="left:515px;top:84px;width:62px;height:70px;background:#1f5a45"></div>
    <div class="partner" style="left:617px;top:98px;width:156px;height:46px;background:#b8b8b8"></div>
    <div class="partner" style="left:804px;top:90px;width:65px;height:60px;background:#263f86"></div>
    <div class="partner" style="left:911px;top:90px;width:55px;height:60px;background:#b2342b"></div>
  </section>

  <footer class="copyright">© Morvel Brew Supply, 2014</footer>
</body>
</html>
```